Professional, Attractive, Simple Website Needed!!

We completed the design for our logo.

We need a website built out around this.

Here are a couple samples of how we want ours formatted.

http://brvntapower.com

http://www.halvorbeam.com/lp/free-quote?LeadSource=Search%20Engine&ProgramName=webquery&experience=qual&language=en&type=brd&gclid=Xq7RTPwmEYKDLAvUHbsNQkfPZrTcGwnJuoVbXeLqHmRYdAsWtPkMcNfBYgzTrUoQJhEdWvKpYaLsZbCmNDgQwTxAoKpXbT_qkR

http://morvalo.co

Reason: Extending this deadline due to our delay in providing designers with content for each page. This is coming in next 24 hours.

Reason: Due to scheduling conflicts and extended travel delays related to Puerto Rico, the deadline has been extended. Your patience is greatly appreciated.

Reason: Travel and scheduling conflicts have made it impossible to give this project the thorough review it deserves, therefore I am extending the deadline. Thank you for your patience!

Target Market(s)

Home Owners who earn 60k + household annually

Industry/Entity Type

It Professional

Coding

Coded - Design and coding required

Number of Pages Required

5+ page

Font styles to use
Serif

Colors
34a7d8
9bcb3c

Requirements
Must have
• Simple
• Lead form Entry (Ability for visitor to enter Name, number and address for a quote)
• Sleek Design
• Professional
• Testimonials
• Use color Scheme of Design Logo Attached
Nice to have
• Video when site starts
• Like this
• https://www.vidmarrow.com/watch?v=qT8mRpXw2Ka&feature=vidm.ro
Should not have
• Should not include Commercial solar
• Should not include wind power

```html
<!DOCTYPE html>
<html lang="en">
<head>
<meta charset="utf-8">
<title>Sunmere Energy — Home Solar</title>
<link href="https://fonts.googleapis.com/css2?family=Lato:wght@400;700;900&display=swap" rel="stylesheet">
<style>
  :root {
    --blue: #1e8fd0;
    --blue-dark: #1a6fc2;
    --green: #8dc63f;
    --green-line: #9bcb3c;
    --topbar: #e1edc3;
    --ink: #222;
    --nav-ink: #333;
    --white: #fff;
  }
  * { margin: 0; padding: 0; box-sizing: border-box; }
  html, body { width: 1200px; height: 1200px; overflow: hidden; background: var(--white); font-family: "Lato", sans-serif; }
  .page { position: relative; width: 1200px; height: 1200px; }

  .topbar { position: absolute; top: 0; left: 0; width: 1200px; height: 70px; background: var(--topbar); border-top: 2px solid var(--blue); box-shadow: 0 2px 4px rgba(0,0,0,.08); }
  .phone { position: absolute; left: 154px; top: 20px; display: flex; align-items: center; gap: 8px; }
  .phone-icon { width: 32px; height: 32px; background: #eef4dd; border: 1px solid #cfdcb0; display: flex; align-items: center; justify-content: center; }
  .phone-number { font-size: 12.5px; font-weight: 700; color: var(--blue-dark); letter-spacing: .3px; }

  .nav { position: absolute; top: 25px; left: 698px; display: flex; gap: 19px; font-size: 14px; color: var(--nav-ink); }
  .nav .active { color: var(--blue); }

  .brand { position: absolute; left: 500px; top: 14px; width: 200px; text-align: center; }
  .brand-mark { width: 92px; height: 92px; margin: 0 auto; border-radius: 50%; background: var(--white); border: 4px solid var(--blue); }
  .brand-name { margin-top: 8px; font-size: 22px; font-weight: 700; color: var(--blue); letter-spacing: .2px; }

  .zip-search { position: absolute; left: 862px; top: 104px; width: 216px; height: 29px; border: 2px solid #e6e6e6; border-radius: 15px; display: flex; align-items: center; font-size: 13px; color: #999; padding-left: 14px; }
  .zip-search .search-btn { position: absolute; right: 0; top: 2px; width: 29px; height: 21px; border-left: 1px solid #ddd; display: flex; align-items: center; justify-content: center; }

  .hero { position: absolute; top: 174px; left: 0; width: 1200px; height: 490px;
    background: linear-gradient(180deg, #3f84c6 0%, #8fbfe0 25%, #f4eed2 47%, #d9c9c8 52%, #5a5f9e 64%, #2c3d8e 100%); }
  .hero-badge { position: absolute; left: 150px; top: 99px; width: 292px; height: 292px; border-radius: 50%; background: rgba(35,40,48,.78); text-align: center; color: var(--white); }
  .hero-badge h1 { margin-top: 54px; font-size: 29px; font-weight: 700; letter-spacing: .5px; }
  .hero-badge p { margin: 12px auto 0; width: 210px; font-size: 12px; line-height: 24px; }
  .btn-info { display: inline-block; margin-top: 17px; width: 161px; height: 40px; line-height: 40px; border-radius: 3px; background: linear-gradient(180deg, #3b8fe0, #1f66c4); font-size: 15px; color: var(--white); }

  .benefits-title { position: absolute; top: 732px; left: 0; width: 1200px; text-align: center; font-size: 32px; font-weight: 900; color: var(--ink); letter-spacing: 1px; }
  .benefits-title span { color: var(--blue); }
  .title-rule { position: absolute; left: 583px; top: 771px; width: 80px; height: 2px; background: var(--green-line); }

  .benefit { position: absolute; top: 844px; width: 304px; height: 304px; border-radius: 50%; background: radial-gradient(circle at 50% 45%, #4a5350 0%, #2a2f33 60%, #16191b 100%); text-align: center; color: var(--white); box-shadow: 0 3px 6px rgba(0,0,0,.15); }
  .benefit h2 { margin-top: 62px; font-size: 21px; font-weight: 900; color: var(--blue); }
  .benefit p { margin: 14px auto 0; width: 265px; font-size: 14px; line-height: 20px; }
  .btn-more { position: absolute; left: 93px; top: 242px; width: 117px; height: 34px; border-radius: 17px; background: var(--green); font-size: 14px; color: var(--white); display: flex; align-items: center; justify-content: center; gap: 8px; }
</style>
</head>
<body>
<div class="page">
  <header class="topbar">
    <div class="phone">
      <span class="phone-icon">
        <svg width="18" height="18" viewBox="0 0 24 24"><path fill="#1e8fd0" d="M6.6 10.8a15 15 0 0 0 6.6 6.6l2.2-2.2c.3-.3.7-.4 1-.2 1.1.4 2.3.6 3.6.6.6 0 1 .4 1 1V20c0 .6-.4 1-1 1A17 17 0 0 1 3 4c0-.6.4-1 1-1h3.5c.6 0 1 .4 1 1 0 1.3.2 2.5.6 3.6.1.3 0 .7-.2 1l-2.3 2.2z"/></svg>
      </span>
      <span class="phone-number">1.800.555.0142</span>
    </div>
    <nav class="nav">
      <span>Home</span><span class="active">Why Solar</span><span>Partnerships</span><span>Blog</span><span>Faq</span><span>Contact</span>
    </nav>
  </header>

  <div class="brand">
    <div class="brand-mark"></div>
    <div class="brand-name">Sunmere Energy</div>
  </div>

  <div class="zip-search">Enter your ZIP code.
    <span class="search-btn">
      <svg width="12" height="12" viewBox="0 0 24 24"><circle cx="10" cy="10" r="6.5" fill="none" stroke="#1e8fd0" stroke-width="3"/><path d="M15 15l6 6" stroke="#1e8fd0" stroke-width="3"/></svg>
    </span>
  </div>

  <section class="hero" role="img" aria-label="Photo of rooftop solar panel rows under a bright sunrise sky">
    <div class="hero-badge">
      <h1>HUGE SAVING</h1>
      <p>While minimizing your risk, we help you maximize the potential of your home to become the best home possible.</p>
      <span class="btn-info">MORE INFO &gt;&gt;</span>
    </div>
  </section>

  <h2 class="benefits-title">HOW <span>YOU BENEFIT</span></h2>
  <div class="title-rule"></div>

  <article class="benefit" style="left:122px" role="img" aria-label="Photo of a couple reviewing paperwork">
    <h2>ZERO COST</h2>
    <p>It is a long established fact that a reader will be distracted by the readable content of a page when looking at its layout. The point of using Lorem Ipsum is that</p>
    <span class="btn-more">Read More <svg width="15" height="12" viewBox="0 0 15 12"><path d="M1 6h12M8 1l5 5-5 5" fill="none" stroke="#fff" stroke-width="2.2"/></svg></span>
  </article>

  <article class="benefit" style="left:449px" role="img" aria-label="Photo of hands holding a young green sprout">
    <h2>LOWER BILLS</h2>
    <p>It is a long established fact that a reader will be distracted by the readable content of a page when looking at its layout. The point of using Lorem Ipsum is that</p>
    <span class="btn-more">Read More <svg width="15" height="12" viewBox="0 0 15 12"><path d="M1 6h12M8 1l5 5-5 5" fill="none" stroke="#fff" stroke-width="2.2"/></svg></span>
  </article>

  <article class="benefit" style="left:774px" role="img" aria-label="Photo of a technician installing solar panels">
    <h2>NO MAINTENANCE</h2>
    <p>It is a long established fact that a reader will be distracted by the readable content of a page when looking at its layout. The point of using Lorem Ipsum is that</p>
    <span class="btn-more">Read More <svg width="15" height="12" viewBox="0 0 15 12"><path d="M1 6h12M8 1l5 5-5 5" fill="none" stroke="#fff" stroke-width="2.2"/></svg></span>
  </article>
</div>
</body>
</html>
```